Retailer of Global Mobile Credit Web Redesign

We need a professional redesign (photoshop only - no coding) of an existing ecommerce website. Currently the website runs on Wordpress with woocommerce. We would like to keep that setup.
The attached draft shows a very crude mockup of ideas for the homepage. These are ideas only - we value your creative suggestions. I have also attached a preliminary logo, but this will likely be changed, so please don't base your color choices on it.
The draft also gives you the URL of the current site.
One of the sites which has a design we like it globexsend.net.
The design is for ten pages - two of which are templates.
1. Homepage. Please see the attached draft for ideas. We like a darker picture with white lettering for the top of the page like Pennaroute.com. The photo is just to give color, it is not meant to capture the user's attention but just be a background.
2. Countries page (/countries/). We need an elegant, easily navigable way to show the countries where we offer credit and the operators we offer for that country. If you feel that it is better to delete the countries page and instead show that information when you click "countries" in the menu, then please design how the menu would look.
3. How It Works (/how-it-works/)
4. My Account (/account-info/) prior to logging in or registering)
5. My Account (/account-info) after logging in
6. Privacy (/privacy/). A basic page with text.
7. Checkout (/checkout/). You won't have access to this page but I've attached a screenshot that shows you all the elements of the checkout page.
8. /how-to-sell-phone-credit/
9. /ghana/ Your design for this page will be used as a template for all the country pages e.g. /antigua/ and /el-salvador/
10. /product/recharge-qvr-ghana/ Your design for this page will be used as a template for all operator pages e.g. /product/recharge-vexlo-ghana/ or /product/recharge-brindo-costa-rica/
Thank you in advance for your submissions. Be sure to let us know if you have any questions.
Reason: Hello, I was on holiday. I like the design very much and look forward to finalizing it.

```html
<!DOCTYPE html>
<html lang="en">
<head>
<meta charset="utf-8">
<title>Checkout – Topvolt Club</title>
<link href="https://fonts.googleapis.com/css2?family=Signika:wght@400;600&family=Arimo:wght@400;700&display=swap" rel="stylesheet">
<style>
:root{
  --blue:#1a71b8;
  --blue-dark:#125c99;
  --orange:#f97d1f;
  --ink:#222;
  --muted:#777;
  --line:#c9c9c9;
  --panel:#e3e3e3;
  --white:#fff;
}
*{box-sizing:border-box;margin:0;padding:0}
html,body{width:709px;height:1200px;overflow:hidden;background:var(--white)}
body{position:relative;font-family:"Arimo",Arial,sans-serif;color:var(--ink)}
.abs{position:absolute}
.site-header{left:0;top:0;width:709px;height:63px}
.brand{left:36px;top:16px;font-family:"Signika",sans-serif;font-weight:600;font-size:27px;color:var(--blue);letter-spacing:1px}
.social{left:469px;top:24px;display:flex;gap:4px}
.social span{width:14px;height:14px;border-radius:50%;background:#111;display:block}
.login{left:566px;top:28px;font-size:9px;font-family:"Signika",sans-serif}
.signup{left:608px;top:23px;width:65px;height:21px;background:var(--orange);color:#fff;font-family:"Signika",sans-serif;font-size:9px;display:flex;align-items:center;justify-content:center}
.nav{left:0;top:63px;width:709px;height:30px;background:var(--blue)}
.nav ul{list-style:none;display:flex;position:absolute;left:48px;top:11px;gap:0}
.nav li{font-family:"Signika",sans-serif;font-size:8px;color:#fff;margin-right:27px}
.search{left:538px;top:69px;width:136px;height:19px;background:#fff}
.search svg{position:absolute;right:5px;top:3px}
.hero{left:0;top:93px;width:709px;height:134px;background:linear-gradient(90deg,#3d3f57 0%,#7a6370 35%,#c98a80 60%,#5e5468 100%)}
.crumb{left:0;top:227px;width:709px;height:25px;background:var(--orange);color:#fff;font-family:"Signika",sans-serif;font-size:9px;padding:8px 0 0 35px}
.page-title{left:0;top:272px;width:709px;text-align:center;font-family:"Signika",sans-serif;font-size:22px}
.steps{left:200px;top:322px}
.step-label{top:369px;font-family:"Signika",sans-serif;font-size:10.5px;color:#444;text-align:center;width:120px}
.panel{border:1px solid var(--line)}
.billing{left:36px;top:436px;width:361px;height:408px}
.panel h2{font-family:"Signika",sans-serif;font-weight:400;font-size:15px;color:var(--blue)}
.field{height:24px;border:1px solid var(--line);border-radius:12px;font-size:8px;color:var(--muted);padding:7px 0 0 9px;box-shadow:0 1px 2px rgba(0,0,0,.12)}
.country{left:55px;top:593px;font-size:8px;font-weight:700}
.register{left:284px;top:806px;width:85px;height:23px;border-radius:12px;background:var(--orange);color:#fff;font-size:8.5px;font-weight:700;display:flex;align-items:center;justify-content:center}
.promo{left:421px;top:436px;width:253px;height:84px}
.promo h3{font-family:"Signika",sans-serif;font-weight:400;font-size:12px;position:absolute;left:18px;top:12px}
.promo-input{left:15px;top:38px;width:211px;height:24px;border:1px solid var(--line);border-radius:12px;font-size:8px;color:var(--muted);padding:7px 0 0 9px;overflow:hidden}
.promo-input b{position:absolute;right:0;top:0;width:58px;height:24px;background:var(--blue);color:#fff;font-size:8.5px;display:flex;align-items:center;justify-content:center;border-radius:0 12px 12px 0}
.order{left:421px;top:549px;width:253px;height:153px}
.order-head{left:0;top:34px;width:251px;height:22px;background:var(--panel);font-family:"Signika",sans-serif;font-size:11.5px}
.order .row{left:13px;width:212px;font-size:7.5px;display:flex;justify-content:space-between}
.order-total{left:0;top:127px;width:251px;border-top:1px solid var(--line);padding:6px 38px 0 14px;display:flex;justify-content:space-between;font-size:8px;font-weight:700}
.order-total span:first-child{font-family:"Signika",sans-serif;font-size:11px;font-weight:600}
.pay-label{left:44px;top:873px;font-family:"Signika",sans-serif;font-size:10.5px}
.pay-label a{color:var(--blue);font-weight:600;text-decoration:none}
.pay-note{left:43px;top:893px;font-family:"Signika",sans-serif;font-size:10.5px;color:#333}
.cards{left:500px;top:877px;width:174px;height:39px;border:1px solid var(--line)}
.cards-name{left:508px;top:870px;background:#fff;padding:0 3px;font-family:"Signika",sans-serif;font-size:9px;font-weight:600;color:var(--blue-dark)}
.cards .slot{position:absolute;top:9px;width:36px;height:25px;background:#e8e8e8;border:1px solid #ccc}
.terms{left:46px;top:936px;font-family:"Signika",sans-serif;font-size:10px;color:#444;display:flex;align-items:center;gap:9px}
.terms i{width:9px;height:9px;border:1px solid #999;display:block}
.terms a{color:var(--blue);text-decoration:none}
.proceed{left:45px;top:970px;width:158px;height:30px;border-radius:15px;background:var(--orange);color:#fff;font-size:8.5px;font-weight:700;display:flex;align-items:center;justify-content:center}
.footer{left:0;top:1060px;width:709px;height:140px;background:var(--blue);color:#fff;text-align:center}
.footer-brand{position:absolute;left:0;top:22px;width:709px;font-family:"Signika",sans-serif;font-weight:600;font-size:20px;letter-spacing:1px}
.footer-links{position:absolute;left:0;top:59px;width:709px;font-family:"Signika",sans-serif;font-size:10px}
.footer-links span{margin:0 12px}
.copy{position:absolute;left:0;top:79px;width:709px;font-size:8.5px}
.footer-cards{position:absolute;left:295px;top:104px;display:flex;gap:5px}
.footer-cards span{width:22px;height:14px;background:#f2f2f2;border-radius:2px;display:block}
</style>
</head>
<body>
<header class="abs site-header">
  <div class="abs brand">TOPVOLT CLUB</div>
  <div class="abs social"><span></span><span></span><span></span><span></span></div>
  <div class="abs login">LOGIN</div>
  <div class="abs signup">SIGN UP</div>
</header>
<nav class="abs nav">
  <ul><li>HOME</li><li>ABOUT US</li><li>HOW IT WORKS</li><li>HOW-TO-SELL-PHONE-CREDIT</li><li>CONTACT US</li></ul>
</nav>
<div class="abs search">
  <svg width="13" height="13" viewBox="0 0 13 13"><circle cx="5.5" cy="5.5" r="4.2" fill="none" stroke="#111" stroke-width="1.6"/><line x1="8.6" y1="8.6" x2="12" y2="12" stroke="#111" stroke-width="1.8"/></svg>
</div>
<div class="abs hero" role="img" aria-label="Dim photo of hands holding a card above a laptop keyboard"></div>
<div class="abs crumb">Home &nbsp;» &nbsp;Checkout</div>

<h1 class="abs page-title" style="font-weight:400">Checkout</h1>

<svg class="abs steps" width="330" height="46" viewBox="0 0 330 46">
  <defs>
    <pattern id="stripe" width="6" height="6" patternUnits="userSpaceOnUse" patternTransform="rotate(45)">
      <rect width="6" height="6" fill="#1a71b8"/><rect width="3" height="6" fill="#5a9fd4"/>
    </pattern>
    <pattern id="stripeO" width="6" height="6" patternUnits="userSpaceOnUse" patternTransform="rotate(45)">
      <rect width="6" height="6" fill="#f97d1f"/><rect width="3" height="6" fill="#fbb27a"/>
    </pattern>
  </defs>
  <rect x="7" y="19" width="280" height="5" rx="2.5" fill="url(#stripe)"/>
  <rect x="286" y="19" width="38" height="5" rx="2.5" fill="url(#stripeO)"/>
  <g font-family="Signika, sans-serif" font-weight="600" font-size="18" fill="#fff" text-anchor="middle">
    <circle cx="41" cy="22" r="19" fill="#1a71b8" stroke="#fff" stroke-width="2"/><text x="41" y="29">1</text>
    <circle cx="167" cy="22" r="19" fill="#1a71b8" stroke="#fff" stroke-width="2"/><text x="167" y="29">2</text>
    <circle cx="286" cy="22" r="19" fill="#f97d1f" stroke="#fff" stroke-width="2"/><text x="286" y="29">3</text>
  </g>
</svg>
<div class="abs step-label" style="left:181px">Choose a recharge</div>
<div class="abs step-label" style="left:309px">Login/Register</div>
<div class="abs step-label" style="left:427px">Checkout</div>

<section class="abs panel billing">
  <h2 class="abs" style="left:15px;top:10px">Billing Details</h2>
</section>
<div class="abs field" style="left:50px;top:478px;width:145px">Dana Mercer</div>
<div class="abs field" style="left:221px;top:478px;width:146px">Orlin</div>
<div class="abs field" style="left:50px;top:514px;width:317px">Northpine Studio</div>
<div class="abs field" style="left:51px;top:553px;width:145px">dana.mercer@postlane.net</div>
<div class="abs field" style="left:222px;top:553px;width:145px">5550142387</div>
<div class="abs country">United States (US)</div>
<div class="abs field" style="left:50px;top:618px;width:318px">12 Harrow Lane Ridge road</div>
<div class="abs field" style="left:50px;top:661px;width:318px">Apartment, suite, unit etc.(optional)</div>
<div class="abs field" style="left:50px;top:696px;width:318px">Westbrook</div>
<div class="abs field" style="left:50px;top:731px;width:318px">Select an option...
  <svg class="abs" style="right:12px;top:9px" width="8" height="6" viewBox="0 0 8 6"><path d="M0 0H8L4 6Z" fill="#666"/></svg>
</div>
<div class="abs field" style="left:50px;top:765px;width:318px">40217</div>
<div class="abs register">REGISTER</div>

<section class="abs panel promo">
  <h3>Have a Promocode? Apply here!</h3>
  <div class="abs promo-input">Enter Promo code<b>APPLY</b></div>
</section>

<section class="abs panel order">
  <h2 class="abs" style="left:11px;top:10px">Your order</h2>
  <div class="abs order-head"><span class="abs" style="left:13px;top:4px">Product</span><span class="abs" style="left:186px;top:4px">Total</span></div>
  <div class="abs row" style="top:68px"><span>Account Funds Top-up &nbsp;&nbsp;&nbsp;× 1</span><span>$20.00</span></div>
  <div class="abs row" style="top:88px"><span>Subtotal</span><span>$20.00</span></div>
  <div class="abs row" style="top:107px"><span>Transaction Fee</span><span>$00.00</span></div>
  <div class="abs order-total"><span>Total</span><span>$20.00</span></div>
</section>

<div class="abs pay-label">PayGlide <a>What is PayGlide?</a></div>
<div class="abs pay-note">Pay via PayGlide; you can pay with your credit card if you don’t have a PayGlide account.</div>
<div class="abs cards">
  <span class="slot" style="left:6px"></span><span class="slot" style="left:50px"></span><span class="slot" style="left:94px"></span><span class="slot" style="left:131px"></span>
</div>
<div class="abs cards-name">PayGlide</div>

<div class="abs terms"><i></i><span>I’ve read and accept the <a>terms &amp; conditions</a> *</span></div>
<div class="abs proceed">PROCEED TO PAYGLIDE</div>

<footer class="abs footer">
  <div class="footer-brand">TOPVOLT CLUB</div>
  <div class="footer-links">Terms<span>|</span>Contact<span>|</span>Privacy</div>
  <div class="copy">Copyright © 2016 Topvolt Club. All Rights Reserved.</div>
  <div class="footer-cards"><span></span><span></span><span></span><span></span><span></span></div>
</footer>
</body>
</html>
```